Bookcover: Lessons From the Silent Orchard

I am publishing a super-low-cost innovation book for €4,99 on Bravolo Self Release to help everyone become a great innovator: young ambitious people without college education nor a big budget. Do you want to help me?

Brief:
Design a book cover 1600 x 2560 pixels for BSR.
Main title: Lessons From the Silent Orchard
Sub title: mindset - insights - skills & tools
Author: Maarten de Klerk
Design: captive, and appealing to everyone
Target Group: young ambitious people without college education

For bravolo please format the height/width ratio of 1.6:1

```html
<!DOCTYPE html>
<html lang="en">
<head>
<meta charset="utf-8">
<title>Lessons From the Silent Orchard — Book Cover</title>
<link href="https://fonts.googleapis.com/css2?family=Bebas+Neue&display=swap" rel="stylesheet">
<style>
  :root {
    --cover-yellow: #FFD000;
    --ink-navy: #0D0D33;
    --ink-black: #000000;
    --paper-white: #FFFFFF;
  }
  html, body {
    margin: 0;
    padding: 0;
    width: 750px;
    height: 1200px;
    overflow: hidden;
    background: var(--cover-yellow);
  }
  .book-cover {
    position: relative;
    width: 750px;
    height: 1200px;
    background: var(--cover-yellow);
    font-family: "Bebas Neue", "Arial Narrow", sans-serif;
  }
  .cover-art {
    position: absolute;
    inset: 0;
    width: 750px;
    height: 1200px;
  }
  .accent-line { stroke: var(--ink-navy); stroke-width: 4; }
  .title-panel { fill: var(--ink-navy); }
  .subtitle-band { fill: var(--paper-white); }
  .title-lead { fill: var(--ink-black); font-size: 104px; }
  .title-main { fill: var(--cover-yellow); font-size: 262px; }
  .title-tail { fill: var(--cover-yellow); font-size: 90px; }
  .subtitle { fill: var(--ink-black); font-size: 60px; }
  .author-name {
    position: absolute;
    left: 0;
    right: 0;
    top: 1070px;
    margin: 0;
    text-align: center;
    font-size: 82px;
    line-height: 1;
    letter-spacing: 1px;
    color: var(--ink-black);
    font-weight: 400;
  }
</style>
</head>
<body>
  <main class="book-cover">
    <svg class="cover-art" viewBox="0 0 750 1200" xmlns="http://www.w3.org/2000/svg">
      <line class="accent-line" x1="0" y1="353" x2="481" y2="271"/>
      <line class="accent-line" x1="0" y1="373" x2="557" y2="277"/>
      <line class="accent-line" x1="298" y1="826" x2="750" y2="747"/>
      <line class="accent-line" x1="373" y1="833" x2="750" y2="766"/>

      <polygon class="subtitle-band" points="78,766 641,670 636,742 74,837"/>
      <polygon class="title-panel" points="80,455 693,351 671,665 57,770"/>

      <g transform="translate(131,436) rotate(-9.6)">
        <text class="title-lead" x="0" y="0" textLength="508" lengthAdjust="spacingAndGlyphs">LESSONS FROM THE</text>
      </g>
      <g transform="translate(149,643) rotate(-9.6)">
        <text class="title-main" x="0" y="0" textLength="442" lengthAdjust="spacingAndGlyphs">SILENT</text>
      </g>
      <g transform="translate(149,733) rotate(-9.6)">
        <text class="title-tail" x="0" y="0" textLength="445" lengthAdjust="spacing">ORCHARD</text>
      </g>
      <g transform="translate(102,811) rotate(-9.6)">
        <text class="subtitle" x="0" y="0" textLength="526" lengthAdjust="spacingAndGlyphs">MINDSET - INSIGHTS - SKILLS &amp; TOOLS</text>
      </g>
    </svg>
    <p class="author-name">Maarten de Klerk</p>
  </main>
</body>
</html>
```